Design a New Business Card for Our Company

We are looking for fresh, unique, and a modern business card that reflects our roots as digital marketing agency focused on SEM.

Industry/Entity Type

Marketing

Contact Information for Business Card

looking for very unique out of the box designs. clean and modern that compliments our logo

Requirements
Must have
• colors should match our logo
• Front should have name, address, email, and phone/fax of the person, phone/fax are the same number
• back should have our url

```html
<!DOCTYPE html>
<html lang="en">
<head>
<meta charset="utf-8">
<title>Kestrel Reach — Business Card</title>
<link rel="stylesheet" href="https://fonts.googleapis.com/css2?family=Source+Sans+3:wght@400;600;700&display=swap">
<style>
  :root {
    --stage: #2b2b2b;
    --card-white: #ffffff;
    --card-grey: #a9a9a9;
    --brand-blue: #4f8fd0;
    --text-grey: #8c8c8c;
    --rule-grey: #c8c8c8;
    --dot-white: #ffffff;
  }
  * { box-sizing: border-box; margin: 0; padding: 0; }
  html, body { width: 1200px; height: 751px; overflow: hidden; }
  body {
    background: var(--stage);
    font-family: "Source Sans 3", "Myriad Pro", sans-serif;
    position: relative;
  }
  .card {
    position: absolute;
    width: 500px;
    height: 286px;
    top: 232px;
    box-shadow: 0 10px 24px rgba(0,0,0,.45);
  }

  /* Back */
  .card-back { left: 60px; background: var(--card-grey); }
  .back-mark {
    position: absolute; left: 46px; top: 58px;
    width: 170px; height: 170px; border-radius: 50%;
    background: var(--dot-white);
  }
  .back-brand {
    position: absolute; right: 34px; top: 120px; text-align: right;
  }
  .back-brand .wordmark {
    font-weight: 700; font-size: 40px; line-height: 1; color: var(--dot-white);
    letter-spacing: -0.5px;
  }
  .back-brand .url {
    margin-top: 6px; font-size: 14px; color: var(--dot-white); font-weight: 600;
  }

  /* Front */
  .card-front { left: 640px; background: var(--card-white); }
  .front-brand {
    position: absolute; left: 30px; top: 56px;
    display: flex; align-items: center; gap: 10px;
  }
  .front-brand .dot {
    width: 28px; height: 28px; border-radius: 50%; background: var(--brand-blue);
  }
  .front-brand .wordmark {
    font-weight: 700; font-size: 34px; line-height: 1; color: var(--brand-blue);
    letter-spacing: -0.5px;
  }
  .phones {
    position: absolute; right: 26px; top: 44px; text-align: right;
    font-size: 12px; color: var(--text-grey); line-height: 20px;
  }
  .phones li { list-style: none; display: flex; align-items: center; justify-content: flex-end; gap: 6px; }
  .phones li + li { border-top: 1px solid var(--rule-grey); }
  .icon { width: 13px; height: 13px; flex: none; }
  .rule-blue {
    position: absolute; left: 30px; right: 26px; top: 118px;
    height: 1px; background: var(--brand-blue);
  }
  .person { position: absolute; left: 30px; top: 140px; }
  .person .name { font-weight: 700; font-size: 16px; color: var(--brand-blue); }
  .person .role { font-size: 12px; color: var(--text-grey); }
  .links {
    position: absolute; left: 30px; top: 196px;
    font-size: 12px; color: var(--text-grey); line-height: 17px;
  }
  .links li { list-style: none; display: flex; align-items: center; gap: 6px; }
  .rule-grey {
    position: absolute; left: 30px; right: 26px; top: 236px;
    height: 1px; background: var(--rule-grey);
  }
  .address {
    position: absolute; right: 26px; top: 244px;
    font-size: 12.5px; color: var(--brand-blue);
  }
</style>
</head>
<body>
  <section class="card card-back" aria-label="Card back">
    <div class="back-mark"></div>
    <div class="back-brand">
      <div class="wordmark">Kestrel Reach</div>
      <div class="url">www.kestrelreach.com</div>
    </div>
  </section>

  <section class="card card-front" aria-label="Card front">
    <div class="front-brand">
      <span class="dot"></span>
      <span class="wordmark">Kestrel Reach</span>
    </div>

    <ul class="phones">
      <li>555.010.234
        <svg class="icon" viewBox="0 0 14 14"><circle cx="7" cy="7" r="7" fill="#4f8fd0"/><path d="M4.5 4h1.6l.6 1.6-.9.7a5 5 0 0 0 1.9 1.9l.7-.9 1.6.6V9.5A.7.7 0 0 1 9.3 10 5.6 5.6 0 0 1 4 4.7.7.7 0 0 1 4.5 4z" fill="#fff"/></svg>
      </li>
      <li>555.010.234
        <svg class="icon" viewBox="0 0 14 14"><circle cx="7" cy="7" r="7" fill="#4f8fd0"/><rect x="3.5" y="6" width="7" height="4" rx=".6" fill="#fff"/><rect x="5" y="3.6" width="4" height="2.6" fill="#fff"/></svg>
      </li>
    </ul>

    <div class="rule-blue"></div>

    <div class="person">
      <div class="name">Dana Whitfield</div>
      <div class="role">Owner</div>
    </div>

    <ul class="links">
      <li>
        <svg class="icon" viewBox="0 0 14 14"><circle cx="7" cy="7" r="7" fill="#4f8fd0"/><rect x="3.5" y="4.5" width="7" height="5" fill="#fff"/><path d="M3.5 4.5 7 7.5l3.5-3" fill="none" stroke="#4f8fd0" stroke-width=".8"/></svg>
        hello@kestrelreach.com
      </li>
      <li>
        <svg class="icon" viewBox="0 0 14 14"><circle cx="7" cy="7" r="7" fill="#4f8fd0"/><circle cx="7" cy="7" r="3.6" fill="none" stroke="#fff" stroke-width=".9"/><path d="M3.4 7h7.2M7 3.4c-1.6 2-1.6 5.2 0 7.2M7 3.4c1.6 2 1.6 5.2 0 7.2" fill="none" stroke="#fff" stroke-width=".7"/></svg>
        www.kestrelreach.com
      </li>
    </ul>

    <div class="rule-grey"></div>

    <p class="address">N. 4 Sample Road, Suite 200, Boise, ID 83700</p>
  </section>
</body>
</html>
```